Pina Colada Paradise, Take-a-Vacation Postcard

I'm a freelance pharmaceutical copywriter trying to attract new clients before the end of the summer vacation season. I have a creative commons stock photo already picked out, I need a skilled designer to incorporate the included copy. As far as tonality, I would like to communicate a professional and energetic mood to counter-balance the visual. A little Caribbean whimsy might be cool to carry over to the back. Please try to keep the line breaks on the front headline as is. I've indicated on the copy that my contact information must be prominent. Not used car salesman-like, but tasteful and in tone with the rest of the layout. I'm selling my ability to write, so an easy-to-read font is a priority. I like the color palate of the picture. Also: Please design according to Harlow Mail Specifications for Oversize 8.52" x 5.47" Postcard.P.S. August is right around the corner, so timing is a huge priority.
Updates
Please conform to Harlow Mail design standards for 5 1/2 x 8 1/2 postcard Added Wednesday, July 29, 2015
Target Market(s)
NYC Creative Directors
Industry/Entity Type
Pharmaceutical
Requirements
Must have
- Harlow Mail Specs for 5 1/2" x 8 1/2" Post Card (room for address, postage.)
- Prominent, but not "loud" contact information on back.
- I need to come across as polished and professional.
Nice to have
- 90% sure I want to use the visual supplied. Info in Project Description.
- (Easy-to-read copy is vital, since I'm selling my writing service). Otherwise, use your imagination.
- NEW AS OF THURS 11:00 PM: If you are unfamiliar with the requirements for the back of the postcard, try this link as a guideline. I've also posted 2 examples under Added Files. Use what I've provided as a guideline. We can make adjustments if necessary.
- http://www.quillandtandem.example/templates/mailing/5.5X8.5_Postcard.pdf
- FRI 7/31 2:20 - If you need further reference, I've added a third postcard example. This is the exact same same size as the on you are working on and conforms to the specifications I need. See uploaded file: "postcard example 3"
Should not have
- Busy layout

```html
<!DOCTYPE html>
<html lang="en">
<head>
<meta charset="utf-8">
<title>Relax – Freelance Copy Postcard</title>
<link rel="stylesheet" href="https://fonts.googleapis.com/css2?family=Open+Sans:wght@300;400;600;700&family=Oswald:wght@300;400;600&display=swap">
<style>
  :root {
    --stage: #3d3b3c;
    --paper: #ffffff;
    --beach-blue: #5fb0e3;
    --beach-sand: #e8dccb;
    --sand-deep: #d8c09c;
    --sand-light: #f6efe4;
    --orange: #d9731f;
    --rust: #b4561a;
    --brown: #6a3d1c;
    --ink: #3a3330;
    --soft-ink: #5f5a56;
    --stamp: #cfcfcf;
  }
  * { box-sizing: border-box; margin: 0; padding: 0; }
  html, body { width: 885px; height: 1200px; overflow: hidden; }
  body {
    background: var(--stage);
    font-family: "Open Sans", Arial, sans-serif;
    position: relative;
  }

  /* ---------- Front ---------- */
  .card-front {
    position: absolute;
    left: 44px; top: 30px;
    width: 797px; height: 525px;
    overflow: hidden;
    background: var(--paper);
  }
  .beach-photo {
    position: absolute; inset: 0;
    background: linear-gradient(180deg, var(--beach-blue) 0%, var(--beach-sand) 100%);
  }
  .front-headline {
    position: absolute; left: 45px; top: 55px;
    color: #fff;
    font-weight: 300;
    font-size: 96px;
    line-height: 1;
    letter-spacing: -1px;
  }
  .front-subline {
    position: absolute; left: 50px; top: 168px;
    color: #fff;
    font-weight: 400;
    font-size: 27px;
  }
  .front-tagline {
    position: absolute; left: 50px; top: 405px;
    color: var(--soft-ink);
    font-weight: 300;
    font-size: 34px;
  }
  .front-tagline strong { font-weight: 700; }

  /* ---------- Back ---------- */
  .card-back {
    position: absolute;
    left: 44px; top: 628px;
    width: 797px; height: 508px;
    background: var(--paper);
    overflow: hidden;
  }
  .sand-photo {
    position: absolute; left: 0; top: 0;
    width: 355px; height: 100%;
    background: linear-gradient(180deg, var(--sand-deep) 0%, var(--sand-light) 100%);
  }
  .back-copy {
    position: absolute; left: 14px; top: 140px;
    width: 330px;
  }
  .back-headline {
    font-family: "Oswald", "Arial Narrow", sans-serif;
    font-weight: 400;
    font-size: 33px;
    line-height: 1.02;
    color: var(--orange);
    text-transform: uppercase;
  }
  .back-subline {
    margin-top: 8px;
    font-weight: 700;
    font-size: 18px;
    color: var(--rust);
  }
  .back-intro {
    margin-top: 8px;
    font-size: 11px;
    line-height: 1.4;
    color: var(--ink);
  }
  .provide-title {
    margin-top: 10px;
    font-weight: 700;
    font-size: 13px;
    color: var(--brown);
  }
  .provide-list { list-style: none; margin-top: 4px; }
  .provide-list li {
    position: relative;
    padding-left: 16px;
    font-size: 11px;
    line-height: 1.45;
    color: var(--ink);
  }
  .provide-list li::before {
    content: "";
    position: absolute; left: 2px; top: 5px;
    width: 7px; height: 7px;
    background: var(--orange);
  }
  .back-closing {
    margin-top: 14px;
    font-weight: 700;
    font-size: 17px;
    line-height: 1.25;
    color: var(--rust);
  }

  .return-address {
    position: absolute; left: 370px; top: 24px;
    font-style: normal;
    font-size: 10px;
    line-height: 1.35;
    color: var(--ink);
  }
  .return-address strong { font-weight: 700; }
  .postage-box {
    position: absolute; right: 15px; top: 12px;
    width: 118px; height: 104px;
    background: var(--stamp);
  }
  .contact-block {
    position: absolute; left: 370px; top: 84px;
  }
  .contact-name {
    font-family: "Open Sans", Arial, sans-serif;
    font-size: 29px;
    line-height: 1.08;
    text-transform: uppercase;
  }
  .contact-name .given { display: block; color: var(--orange); font-weight: 400; }
  .contact-name .family { display: block; color: var(--brown); font-weight: 700; }
  .contact-line {
    display: flex; align-items: center; gap: 6px;
    margin-top: 5px;
    color: var(--ink);
  }
  .contact-line.phone { margin-top: 6px; font-size: 22px; }
  .contact-line.email { font-size: 11px; }
  .contact-line.web { font-size: 15px; font-weight: 700; color: var(--rust); }
  .contact-line svg { flex: none; }
</style>
</head>
<body>

<section class="card-front">
  <div class="beach-photo" role="img" aria-label="Photo: tropical beach with a red frozen cocktail standing in the sand"></div>
  <h1 class="front-headline">Relax</h1>
  <p class="front-subline">You work on the tan lines</p>
  <p class="front-tagline">I’ll work on the <strong>tag lines...</strong></p>
</section>

<section class="card-back">
  <div class="sand-photo" role="img" aria-label="Photo: the word stress written in beach sand as a wave washes over it"></div>

  <div class="back-copy">
    <h2 class="back-headline">Savor the end<br>of the summer</h2>
    <p class="back-subline">With stress-free freelance copy</p>
    <p class="back-intro">I possess a rare combination of pharma copy expertise and seashore savvy. As such, I can assure you that now is the perfect time to stop writing and start chilling.</p>
    <p class="provide-title">I PROVIDE:</p>
    <ul class="provide-list">
      <li>First rate, first-draft copy</li>
      <li>Pharma instincts with a creative soul</li>
      <li>15 years of senior-level experience</li>
      <li>The battle-tested ability to shoulder a heavy workload</li>
    </ul>
    <p class="back-closing">I’ll put in the quality work so you can have some quality time.</p>
  </div>

  <address class="return-address">
    <strong>Nolan Ashbury</strong><br>
    212 W 74th St, #5<br>
    New York, New York 10023
  </address>
  <div class="postage-box"></div>

  <div class="contact-block">
    <p class="contact-name"><span class="given">Nolan</span><span class="family">Ashbury</span></p>
    <p class="contact-line phone">
      <svg width="16" height="18" viewBox="0 0 16 18" aria-hidden="true"><path d="M3 1h3l1.5 4-2 1.5c1 2.3 2.6 3.9 4.8 5l1.5-2 4 1.5v3c0 1.2-1 2-2 2C7 16 1 10 1 3c0-1 .8-2 2-2z" fill="#d9731f"/></svg>
      732-555-0148
    </p>
    <p class="contact-line email">
      <svg width="13" height="10" viewBox="0 0 13 10" aria-hidden="true"><rect x="0.5" y="0.5" width="12" height="9" fill="none" stroke="#6f6a66"/><path d="M0.5 0.5l6 5 6-5" fill="none" stroke="#6f6a66"/></svg>
      nashbury@mailbox.example
    </p>
    <p class="contact-line web">
      <svg width="12" height="12" viewBox="0 0 12 12" aria-hidden="true"><circle cx="6" cy="6" r="6" fill="#d9731f"/></svg>
      nolanashbury.example
    </p>
  </div>
</section>

</body>
</html>
```